Invitation annual meeting 2017 of Corlimaux Group (2017 Annual Staff Appointments)

Version française: We want to create an invitation to the annual meeting of Groupe Corlimaux. This invitation will also be printed as a poster. You will find enclosed a photo of a "B" made with the employees of the Group during an internal event. You will absolutely have this photo on the invitation. I also send it to you when you save it while waiting for the invitation. The invitation must be festive, elegant and classy, ​​because it will take place on the 18th of December, just before Christmas (on the theme of Christmas and New Year Eve). Please, do not use the color "red" on this invitation. You can use this gray: Pantone 431 C for this invitation if you want to. The annual meeting of the staff (annual meeting) 18 December 2017 (18th) of December 2017) Halloriune (at Halloriune) From 5pm to 9.30pm (from 5pm to 9.30pm) French version: On the occasion of the annual meeting of the staff we wish to make an invitation which will also be printed as a poster. You will find in the attached elements a photo of a B made on the beach with employees. It will be necessary to use this B imperatively for your creation. I am also sending you the quick save the date we had done while waiting for the invitation. This one must be classy, ​​festive because the event will take place on December 18th, with the approach of the end-of-year celebrations (thematic New Year's Eve and non-christmas). You can use anthracite gray: Pantone 431C The group logo should appear on the invitation. Text: Annual Staff Meeting 18 December 2017 Halloriune from 5pm to 9.30pm

Project Deadline Extended Reason: Hello We give two more days on the project because we have not been fully seduced by the proposals received so far. Added Tuesday, October 24, 2017

ENG: Internal ==> employees of the Corlimaux Group FR: internal to the Group

• ENG: It is obligatory to use the photo of the "B" on the beach for this invitation. You can crop the image of the B if you want to. FR: B "made by employees" of the transmitted photo (possibility of detaching it)
• ENG: Boat photos, "kitsch" designs and the color red EN: the pictures of boats, the "kitsch", the red

```html
<!DOCTYPE html>
<html lang="fr">
<head>
<meta charset="UTF-8">
<title>Rendez-vous annuel du personnel — Groupe Corlimaux</title>
<link rel="stylesheet" href="https://fonts.googleapis.com/css2?family=Montserrat:wght@300;400;500;700;800&family=Bebas+Neue&family=Open+Sans:wght@700&display=swap">
<style>
  :root {
    --teal: #1a9e96;
    --navy: #14304d;
    --slate: #2d4a6c;
    --tan: #c9a482;
    --anthracite: #4a5057;
    --paper: #f7f7f8;
    --white: #ffffff;
    --dot-blue: #1d3f78;
  }
  * { margin: 0; padding: 0; box-sizing: border-box; }
  html, body { width: 848px; height: 1200px; overflow: hidden; }
  body { background: var(--paper); }
  .poster {
    position: relative;
    width: 848px;
    height: 1200px;
    overflow: hidden;
    background: linear-gradient(160deg, #ffffff 0%, #f1f1f3 50%, #fafafb 100%);
    font-family: "Montserrat", sans-serif;
  }
  .art { position: absolute; inset: 0; }
  .line { position: absolute; white-space: nowrap; line-height: 1; }
  .brand {
    left: 0; right: 0; top: 48px; text-align: center;
    font-size: 25px; font-weight: 500; letter-spacing: 0.35em;
    color: var(--anthracite);
  }
  .raffle {
    left: 0; right: 0; top: 115px; text-align: center;
    font-family: "Open Sans", sans-serif; font-weight: 700;
    font-size: 19px; color: var(--teal);
  }
  .title-rdv { left: 203px; top: 363px; font-size: 82px; font-weight: 800; color: var(--navy); }
  .title-vous { left: 208px; top: 432px; font-size: 124px; font-weight: 800; color: var(--white); }
  .title-annuel {
    left: 200px; top: 552px; font-family: "Bebas Neue", sans-serif;
    font-size: 131px; color: var(--navy);
  }
  .title-du {
    left: 560px; top: 612px; font-family: "Bebas Neue", sans-serif;
    font-size: 106px; color: var(--navy);
    transform: translate(-50%, -50%) rotate(90deg);
  }
  .title-personnel {
    left: 198px; top: 678px; font-size: 58px; font-weight: 800;
    letter-spacing: 0.04em; color: var(--slate);
  }
  .date-day { left: 58px; top: 912px; font-size: 140px; font-weight: 800; color: var(--teal); letter-spacing: -0.01em; }
  .date-month { left: 60px; top: 1063px; font-size: 29px; font-weight: 800; color: var(--tan); letter-spacing: -0.01em; }
  .date-year { left: 58px; top: 1091px; font-size: 72px; font-weight: 800; color: var(--tan); }
  .divider {
    position: absolute; left: 282px; top: 944px; width: 1.5px; height: 208px;
    background: var(--teal);
  }
  .venue { left: 332px; top: 1039px; font-size: 52px; font-weight: 700; color: var(--teal); }
  .hours { left: 332px; top: 1102px; font-size: 57px; font-weight: 300; color: var(--tan); letter-spacing: 0.01em; }
</style>
</head>
<body>
<main class="poster">
  <svg class="art" width="848" height="1200" viewBox="0 0 848 1200">
    <defs>
      <linearGradient id="crowdTone" x1="0" y1="0" x2="1" y2="0.3">
        <stop offset="0%" stop-color="#7e7b82"/>
        <stop offset="45%" stop-color="#8f8b8d"/>
        <stop offset="80%" stop-color="#b3aaa5"/>
        <stop offset="100%" stop-color="#dccbb8"/>
      </linearGradient>
      <linearGradient id="splashTone" x1="0" y1="0" x2="0" y2="1">
        <stop offset="0%" stop-color="#164a7a"/>
        <stop offset="22%" stop-color="#1aa0b8"/>
        <stop offset="48%" stop-color="#2fbcbf"/>
        <stop offset="68%" stop-color="#1b8c9a"/>
        <stop offset="82%" stop-color="#a8d6cf"/>
        <stop offset="100%" stop-color="#f3ecdc"/>
      </linearGradient>
    </defs>
    <path role="img" aria-label="Photo de la lettre formée par les salariés sur la plage, détourée en éclaboussure florale"
      fill="url(#crowdTone)" opacity="0.85"
      d="M30 270 C60 240 90 250 110 220 C140 250 170 240 200 260 C240 250 280 260 300 270
         C330 220 370 180 390 170 C410 200 440 190 470 180 C500 210 530 220 560 240
         C600 230 640 240 670 290 C700 300 720 340 730 390 C770 420 800 470 820 500
         L848 510 L848 720 C830 760 820 790 820 820 C830 880 820 940 790 985
         C740 960 700 950 660 930 C600 960 540 960 480 950 C420 970 360 950 330 900
         C280 900 240 880 200 850 C160 830 110 800 70 760 C30 730 0 700 0 660
         L0 300 C10 290 20 280 30 270 Z"/>
    <path role="img" aria-label="Fond en aplat dégradé bleu sarcelle vers sable"
      fill="url(#splashTone)"
      d="M130 330 C200 300 260 290 300 292 C320 282 350 288 380 290 C470 280 560 288 630 300
         C650 380 660 440 690 520 C700 600 668 650 660 720 C664 760 650 790 640 800
         C560 808 460 800 380 806 C290 810 210 800 140 796
         C128 700 110 620 120 540 C100 470 132 390 130 330 Z"/>
    <g fill="none" stroke="#ffffff" stroke-width="6">
      <polyline points="344,315 167,315 167,789 641,789 641,315 532,315"/>
    </g>
    <polygon points="344,310 532,310 522,326 354,326" fill="#ffffff"/>
    <circle cx="700" cy="276" r="3" fill="var(--dot-blue)"/>
    <circle cx="712" cy="324" r="5" fill="var(--dot-blue)"/>
  </svg>

  <p class="line brand">GROUPE CORLIMAUX</p>
  <p class="line raffle">TOMBOLA 2 JOURS AU SALON NAUTIQUE DE PORT-LAZARE 2018 À GAGNER</p>

  <h1>
    <span class="line title-rdv">RENDEZ-</span>
    <span class="line title-vous">VOUS</span>
    <span class="line title-annuel">ANNUEL</span>
    <span class="line title-du">DU</span>
    <span class="line title-personnel">PERSONNEL</span>
  </h1>

  <p class="line date-day">18</p>
  <p class="line date-month">DÉCEMBRE</p>
  <p class="line date-year">2017</p>
  <div class="divider"></div>
  <p class="line venue">AU HALLORIUNE</p>
  <p class="line hours">DE 17H À 21H30</p>
</main>
</body>
</html>
```